Redesign Application Page for Job Position

Would like to get a redesign on our Job Application Page.
You can use brennanwardcorp or vellorant as references.

http://www.careersatkpt.example/KPT/NCreateAccount.aspx?aga=qxrtlw4mocHJ7

Target Market(s)

Professional Security Individuals

Industry/Entity Type

Security Guard

Coding

Coded - Design and coding required

Number of Pages Required

1 page

Font styles to use
Sans Serif

Colors
0255a3
3276b5
ffcf3e
fee18a

Requirements
Must have
• User Friendly, Easy Navigation. Must be very easy to read and understand what is required or missing.
Should not have
• Ugly or Bulky

```html
<!DOCTYPE html>
<html lang="en">
<head>
<meta charset="utf-8">
<title>Keypoint Guard Services – Create an Application</title>
<link rel="stylesheet" href="https://fonts.googleapis.com/css2?family=Roboto:wght@400;500;700&family=Montserrat:wght@800&display=swap">
<style>
  :root{
    --page:#e9edf0;
    --card:#ffffff;
    --ink:#1d1f21;
    --muted:#b3b9bd;
    --field:#e8ecee;
    --field-line:#c6cdd1;
    --blue:#3276b5;
    --blue-deep:#0255a3;
    --grey-btn:#c9ccce;
    --help:#e5413b;
    --ghost:#dde2e5;
    --dash:#e1e5e8;
  }
  *{box-sizing:border-box;margin:0;padding:0}
  html,body{width:1200px;height:2786px;overflow:hidden}
  body{background:var(--page);font-family:"Roboto",Arial,sans-serif;color:var(--ink);position:relative}

  .masthead{position:absolute;left:0;top:26px;width:1200px;text-align:center}
  .masthead .company{font-size:20px;font-weight:700;letter-spacing:.5px}
  .masthead .mark{display:block;width:78px;height:78px;margin:26px auto 0;border-radius:50%;background:var(--blue-deep)}
  .masthead .page-title{margin-top:28px;font-size:18px;font-weight:700;letter-spacing:.4px}

  .step-label{position:absolute;right:243px;font-family:"Montserrat",Arial,sans-serif;font-weight:800;font-size:104px;line-height:1;color:var(--ghost);letter-spacing:1px}

  .card{position:absolute;left:243px;width:714px;display:flex;background:var(--card);box-shadow:0 10px 28px rgba(40,60,80,.12)}
  .form{position:relative;width:487px}
  .side{width:227px;display:flex;flex-direction:column;align-items:center;padding:26px 0 30px;box-shadow:-6px 0 18px rgba(40,60,80,.10);position:relative}

  .form h2{position:absolute;left:32px;top:28px;font-size:20px;font-weight:500}
  .date{position:absolute;left:326px;top:28px;display:flex;gap:4px;align-items:center}
  .date span{height:20px;padding:0 6px;background:var(--field);font-size:10px;line-height:20px;text-align:center;min-width:22px}
  .date span.yr{min-width:42px}
  .date svg{margin-left:8px}

  .field{position:absolute}
  .field label,.col-head{display:block;font-size:10px;line-height:13px;color:var(--muted);margin-bottom:6px}
  .input{height:31px;background:var(--field);border:1px solid var(--field-line);position:relative}
  .input svg{position:absolute;right:8px;top:6px}
  .split{display:flex;gap:9px}
  .split .input{flex:none}

  .radio{display:inline-flex;align-items:center;gap:8px;font-size:10px;color:var(--ink)}
  .radio i{width:15px;height:15px;border-radius:50%;border:1px solid #9ba3a8;background:#f4f6f7;position:relative;flex:none}
  .radio.on i::after{content:"";position:absolute;inset:2px;border-radius:50%;background:#8b9398}

  .btn{position:absolute;height:30px;border-radius:15px;display:flex;align-items:center;justify-content:center;gap:12px;font-size:10px;font-weight:500;color:#fff}
  .btn.next{background:var(--blue)}
  .btn.prev{background:var(--grey-btn)}

  .steps{display:flex;gap:20px;font-size:20px;color:#333}
  .steps span{width:26px;height:26px;line-height:26px;text-align:center}
  .steps .current{border:1.5px solid var(--blue);border-radius:50%;color:var(--blue)}
  .dash{width:36px;height:6px;background:var(--dash);margin-top:24px}
  .side .middle{flex:1;display:flex;flex-direction:column;align-items:center;justify-content:center;gap:10px;font-size:13px}
  .side .dash.low{margin:0 0 30px}
  .help{text-align:center}
  .help strong{display:block;color:var(--help);font-size:20px;font-weight:500;margin-bottom:6px}
  .help p{font-size:10px;line-height:16px}

  .subhead{position:absolute;font-size:19px;font-weight:500}
  .license{position:absolute;left:32px;top:182px}
  .license .heads,.license .row{display:grid;grid-template-columns:204px 102px 104px;column-gap:6px}
  .license .row{margin-bottom:5px}
  .license .cell{height:32px;background:var(--field);border:1px solid var(--field-line);font-size:9.5px;line-height:11px;display:flex;align-items:center;padding:0 12px;position:relative}
  .license .cell.date-in{color:var(--muted);padding:0 8px;justify-content:space-between}

  .select{height:31px;background:var(--field);border:1px solid var(--field-line);position:relative}
  .select svg{position:absolute;right:14px;top:12px}

  .languages{position:absolute;left:253px;top:498px;display:grid;grid-template-columns:81px 100px;row-gap:34px}

  .week{position:absolute;left:32px;top:114px;display:grid;grid-template-columns:172px 90px 94px 90px;grid-auto-rows:33.4px;align-items:center;font-size:13px}
</style>
</head>
<body>

<header class="masthead">
  <div class="company">KEYPOINT GUARD SERVICES, INC.</div>
  <span class="mark"></span>
  <div class="page-title">CREATE AN APPLICATION</div>
</header>

<!-- Step 1 -->
<div class="step-label" style="top:266px">Step-1</div>
<section class="card" style="top:353px;height:405px">
  <div class="form">
    <h2>Personal Information</h2>
    <div class="date"><span>05</span><span>01</span><span class="yr">2018</span>
      <svg width="16" height="16" viewBox="0 0 16 16" fill="none" stroke="#8a9399" stroke-width="1.3"><rect x="1.5" y="3" width="13" height="11.5"/><path d="M1.5 6.5h13M5 1v3M11 1v3M4 9h2M7 9h2M10 9h2M4 12h2M7 12h2"/></svg></div>

    <div class="field" style="left:32px;top:72px;width:204px"><label>First Name :</label><div class="input"></div></div>
    <div class="field" style="left:253px;top:72px;width:204px"><label>Middle Name :</label><div class="input"></div></div>
    <div class="field" style="left:32px;top:135px;width:204px"><label>Last Name :</label><div class="input"></div></div>
    <div class="field" style="left:253px;top:135px;width:204px"><label>Gender :</label>
      <div style="display:flex;gap:22px;margin-top:8px"><span class="radio on"><i></i>Male</span><span class="radio"><i></i>Female</span></div></div>
    <div class="field" style="left:32px;top:198px;width:204px"><label>E-mail :</label><div class="input"></div></div>
    <div class="field" style="left:253px;top:198px;width:204px"><label>Contact No. :</label><div class="input">
      <svg width="12" height="18" viewBox="0 0 12 18" fill="none" stroke="#7d868b" stroke-width="1.3"><rect x="1.5" y="1" width="9" height="16" rx="1.5"/><path d="M1.5 13.5h9M4 4h4M4 6.5h4M4 9h4"/></svg></div></div>
    <div class="field" style="left:32px;top:263px;width:204px"><label>Date of Birth :</label>
      <div class="split"><div class="input" style="width:41px"></div><div class="input" style="width:41px"></div><div class="input" style="width:104px"></div></div></div>
    <div class="field" style="left:253px;top:282px;width:204px"><div class="input">
      <svg width="18" height="16" viewBox="0 0 18 16" fill="none" stroke="#7d868b" stroke-width="1.3"><path d="M1 5c0-2 3-3 8-3s8 1 8 3v1h-4V4.5H5V6H1z"/><path d="M3 7l-1 8h14l-1-8z"/><circle cx="9" cy="11" r="2"/></svg></div></div>

    <div class="btn next" style="left:275px;top:346px;width:163px">Next Step
      <svg width="6" height="9" viewBox="0 0 6 9"><path d="M1 1l3.5 3.5L1 8" stroke="#fff" stroke-width="1.5" fill="none"/></svg></div>
  </div>
  <aside class="side">
    <div class="steps"><span class="current">1</span><span>2</span><span>3</span><span>4</span></div>
    <div class="dash"></div>
    <div class="middle">
      <svg width="34" height="26" viewBox="0 0 34 26"><rect x="1" y="4" width="32" height="21" rx="2" fill="var(--blue)"/><rect x="11" y="1" width="12" height="5" rx="1" fill="var(--blue)"/><circle cx="10" cy="13" r="3.2" fill="#fff"/><path d="M5 21c0-3 2.3-4.5 5-4.5s5 1.5 5 4.5z" fill="#fff"/><path d="M19 12h10M19 16h10M19 20h7" stroke="#fff" stroke-width="1.8"/></svg>
      <span>Personal Information</span>
    </div>
    <div class="dash low"></div>
    <div class="help"><strong>Need Help?</strong><p>Call us at: (310) 555-0148<br>and ask for a Human Resource representative.</p></div>
  </aside>
</section>

<!-- Step 2 -->
<div class="step-label" style="top:810px">Step-2</div>
<section class="card" style="top:897px;height:344px">
  <div class="form">
    <h2>Address</h2>
    <div class="date"><span>05</span><span>01</span><span class="yr">2018</span>
      <svg width="16" height="16" viewBox="0 0 16 16" fill="none" stroke="#8a9399" stroke-width="1.3"><rect x="1.5" y="3" width="13" height="11.5"/><path d="M1.5 6.5h13M5 1v3M11 1v3M4 9h2M7 9h2M10 9h2M4 12h2M7 12h2"/></svg></div>

    <div class="field" style="left:32px;top:72px;width:425px"><label>Street :</label><div class="input"></div></div>
    <div class="field" style="left:32px;top:135px;width:204px"><label>City :</label><div class="input"></div></div>
    <div class="field" style="left:253px;top:135px;width:204px"><label>State :</label><div class="input"></div></div>
    <div class="field" style="left:32px;top:198px;width:204px"><label>Zip code :</label><div class="input"></div></div>
    <div class="field" style="left:253px;top:198px;width:204px"><label>Nearest Office :</label><div class="input"></div></div>

    <div class="btn prev" style="left:243px;top:282px;width:104px">
      <svg width="6" height="9" viewBox="0 0 6 9"><path d="M5 1L1.5 4.5 5 8" stroke="#fff" stroke-width="1.5" fill="none"/></svg>Previous</div>
    <div class="btn next" style="left:366px;top:282px;width:102px">Next Step
      <svg width="6" height="9" viewBox="0 0 6 9"><path d="M1 1l3.5 3.5L1 8" stroke="#fff" stroke-width="1.5" fill="none"/></svg></div>
  </div>
  <aside class="side">
    <div class="steps"><span>1</span><span class="current">2</span><span>3</span><span>4</span></div>
    <div class="middle">
      <svg width="30" height="30" viewBox="0 0 30 30" fill="var(--blue)"><rect x="2" y="2" width="17" height="26" rx="1"/><rect x="21" y="8" width="7" height="20" rx="1"/><g fill="#fff"><rect x="5" y="6" width="4" height="3"/><rect x="12" y="6" width="4" height="3"/><rect x="5" y="12" width="4" height="3"/><rect x="12" y="12" width="4" height="3"/><rect x="5" y="18" width="4" height="3"/><rect x="12" y="18" width="4" height="3"/></g></svg>
      <span>Address</span>
    </div>
    <div class="help"><strong>Need Help?</strong><p>Call us at: (310) 555-0148<br>and ask for a Human Resource representative.</p></div>
  </aside>
</section>

<!-- Step 3 -->
<div class="step-label" style="top:1291px">Step-3</div>
<section class="card" style="top:1378px;height:658px">
  <div class="form">
    <h2>Job Information</h2>
    <div class="date"><span>05</span><span>01</span><span class="yr">2018</span>
      <svg width="16" height="16" viewBox="0 0 16 16" fill="none" stroke="#8a9399" stroke-width="1.3"><rect x="1.5" y="3" width="13" height="11.5"/><path d="M1.5 6.5h13M5 1v3M11 1v3M4 9h2M7 9h2M10 9h2M4 12h2M7 12h2"/></svg></div>

    <div class="field" style="left:32px;top:72px;width:204px"><label>Job Position :</label><div class="input"></div></div>
    <div class="field" style="left:253px;top:72px;width:204px"><label>SSN :</label>
      <div class="split"><div class="input" style="width:43px"></div><div class="input" style="width:41px"></div><div class="input" style="width:104px"></div></div></div>

    <div class="subhead" style="left:32px;top:150px">License Details</div>
    <div class="license">
      <div class="heads"><span class="col-head" style="color:#555">Type :</span><span class="col-head" style="color:#555">Number :</span><span class="col-head" style="color:#555">Expiry Date :</span></div>
      <div class="row"><div class="cell">Guard Card</div><div class="cell"></div><div class="cell date-in">(mm/dd/yyyy)<svg width="10" height="10" viewBox="0 0 10 10" fill="none" stroke="#8a9399"><rect x="1" y="2" width="8" height="7"/><path d="M1 4.5h8"/></svg></div></div>
      <div class="row"><div class="cell">Baton</div><div class="cell"></div><div class="cell date-in">(mm/dd/yyyy)<svg width="10" height="10" viewBox="0 0 10 10" fill="none" stroke="#8a9399"><rect x="1" y="2" width="8" height="7"/><path d="M1 4.5h8"/></svg></div></div>
      <div class="row"><div class="cell">Gun Permit</div><div class="cell"></div><div class="cell date-in">(mm/dd/yyyy)<svg width="10" height="10" viewBox="0 0 10 10" fill="none" stroke="#8a9399"><rect x="1" y="2" width="8" height="7"/><path d="M1 4.5h8"/></svg></div></div>
      <div class="row"><div class="cell">Transportation Workers<br>Identification Card (TWIC)</div><div class="cell"></div><div class="cell date-in">(mm/dd/yyyy)<svg width="10" height="10" viewBox="0 0 10 10" fill="none" stroke="#8a9399"><rect x="1" y="2" width="8" height="7"/><path d="M1 4.5h8"/></svg></div></div>
      <div class="row"><div class="cell">Merchant Mariner Credential (MMC)</div><div class="cell"></div><div class="cell date-in">(mm/dd/yyyy)<svg width="10" height="10" viewBox="0 0 10 10" fill="none" stroke="#8a9399"><rect x="1" y="2" width="8" height="7"/><path d="M1 4.5h8"/></svg></div></div>
      <div class="row"><div class="cell">Standards of Training, Certification &amp;<br>Watchkeeping for Seafarers (SCTW)</div><div class="cell"></div><div class="cell date-in">(mm/dd/yyyy)<svg width="10" height="10" viewBox="0 0 10 10" fill="none" stroke="#8a9399"><rect x="1" y="2" width="8" height="7"/><path d="M1 4.5h8"/></svg></div></div>
    </div>

    <div class="subhead" style="left:32px;top:447px">ID Document Type</div>
    <div class="subhead" style="left:253px;top:447px">Additional Languages :</div>
    <div class="field" style="left:32px;top:496px;width:204px"><label>Select :</label>
      <div class="select"><svg width="10" height="6" viewBox="0 0 10 6"><path d="M1 1l4 4 4-4" stroke="#555" stroke-width="1.4" fill="none"/></svg></div></div>
    <div class="languages">
      <span class="radio on"><i></i>Spanish</span><span class="radio"><i></i>French</span>
      <span class="radio"><i></i>Japanese</span><span class="radio"><i></i>Chinese</span>
    </div>

    <div class="btn prev" style="left:243px;top:595px;width:104px">
      <svg width="6" height="9" viewBox="0 0 6 9"><path d="M5 1L1.5 4.5 5 8" stroke="#fff" stroke-width="1.5" fill="none"/></svg>Previous</div>
    <div class="btn next" style="left:366px;top:595px;width:102px">Next Step
      <svg width="6" height="9" viewBox="0 0 6 9"><path d="M1 1l3.5 3.5L1 8" stroke="#fff" stroke-width="1.5" fill="none"/></svg></div>
  </div>
  <aside class="side">
    <div class="steps"><span>1</span><span>2</span><span class="current">3</span><span>4</span></div>
    <div class="dash"></div>
    <div class="middle">
      <svg width="22" height="30" viewBox="0 0 22 30"><rect x="1" y="1" width="20" height="28" rx="1.5" fill="var(--blue)" stroke="var(--blue-deep)" stroke-width="1.2"/></svg>
      <span>Job Information</span>
    </div>
    <div class="dash low"></div>
    <div class="help"><strong>Need Help?</strong><p>Call us at: (310) 555-0148<br>and ask for a Human Resource representative.</p></div>
  </aside>
</section>

<!-- Step 4 -->
<div class="step-label" style="top:2087px">Step-4</div>
<section class="card" style="top:2174px;height:550px">
  <div class="form">
    <h2>Work Availability</h2>
    <div class="date"><span>05</span><span>01</span><span class="yr">2018</span>
      <svg width="16" height="16" viewBox="0 0 16 16" fill="none" stroke="#8a9399" stroke-width="1.3"><rect x="1.5" y="3" width="13" height="11.5"/><path d="M1.5 6.5h13M5 1v3M11 1v3M4 9h2M7 9h2M10 9h2M4 12h2M7 12h2"/></svg></div>

    <span class="col-head" style="position:absolute;left:32px;top:76px">Days :</span>
    <span class="col-head" style="position:absolute;left:195px;top:76px">Shifts :</span>
    <div class="week">
      <span>Sunday</span><span class="radio on"><i></i>Day Shift</span><span class="radio"><i></i>Swing Shift</span><span class="radio"><i></i>Night Shift</span>
      <span>Monday</span><span class="radio"><i></i>Day Shift</span><span class="radio"><i></i>Swing Shift</span><span class="radio"><i></i>Night Shift</span>
      <span>Tuesday</span><span class="radio"><i></i>Day Shift</span><span class="radio"><i></i>Swing Shift</span><span class="radio"><i></i>Night Shift</span>
      <span>Wednesday</span><span class="radio"><i></i>Day Shift</span><span class="radio"><i></i>Swing Shift</span><span class="radio"><i></i>Night Shift</span>
      <span>Thursday</span><span class="radio"><i></i>Day Shift</span><span class="radio"><i></i>Swing Shift</span><span class="radio"><i></i>Night Shift</span>
      <span>Friday</span><span class="radio"><i></i>Day Shift</span><span class="radio"><i></i>Swing Shift</span><span class="radio"><i></i>Night Shift</span>
      <span>Saturday</span><span class="radio"><i></i>Day Shift</span><span class="radio"><i></i>Swing Shift</span><span class="radio"><i></i>Night Shift</span>
    </div>

    <div class="subhead" style="left:32px;top:358px">How did you hear about us?</div>
    <div class="field" style="left:32px;top:408px;width:204px"><label>Select :</label>
      <div class="select"><svg width="10" height="6" viewBox="0 0 10 6"><path d="M1 1l4 4 4-4" stroke="#555" stroke-width="1.4" fill="none"/></svg></div></div>

    <div class="btn prev" style="left:243px;top:489px;width:104px">
      <svg width="6" height="9" viewBox="0 0 6 9"><path d="M5 1L1.5 4.5 5 8" stroke="#fff" stroke-width="1.5" fill="none"/></svg>Previous</div>
    <div class="btn next" style="left:366px;top:489px;width:102px">Continue
      <svg width="6" height="9" viewBox="0 0 6 9"><path d="M1 1l3.5 3.5L1 8" stroke="#fff" stroke-width="1.5" fill="none"/></svg></div>
  </div>
  <aside class="side">
    <div class="steps"><span>1</span><span>2</span><span>3</span><span class="current">4</span></div>
    <div class="dash"></div>
    <div class="middle">
      <svg width="32" height="30" viewBox="0 0 32 30"><rect x="3" y="2" width="26" height="18" rx="1.5" fill="var(--blue)"/><rect x="6" y="5" width="20" height="12" fill="#fff"/><rect x="9" y="8" width="9" height="6" fill="var(--blue)"/><path d="M1 24h30l-2 4H3z" fill="var(--blue)"/></svg>
      <span>Work Availability</span>
    </div>
    <div class="dash low"></div>
    <div class="help"><strong>Need Help?</strong><p>Call us at: (310) 555-0148<br>and ask for a Human Resource representative.</p></div>
  </aside>
</section>

</body>
</html>
```